Borrowed Lanterns - the new thriller in the Tidewater series by award-winning author Marta K. Belloway

Looking for an book cover design for the 4th book in the Tidewater series by Marta K. Belloway. Covers from the first 3 books are attached. Would like to keep a series look going, so possibly using a hand holding a paint brush might work - but not tied down to showing a hand on the cover. Most of the book takes place in a rustic Arizona desert estate in a national forest - so something depicting a desert scene might work too. The cover needs to convey a "thriller" feeling. Attached is our design template with needed specs. Also attached are two other covers for inspiration:

A GARDEN UNDER SALT - something like this could work in the key were a paintbrush and the scene is set in the Arizona desert

THE ORCHARD AT NOON - this could work too with Arizona desert setting

Here's the synopsis of BORROWED LANTERNS:

Her life ended and she is disappointed to discover she is still alive.

With all ties to her handler or anyone connected to her life as a hired killer, she struggles to understand who and even what she has become. She knows she doesn’t want to kill again. And yes, danger finds her and she responds, animal-like, in the only way she knows how.

In this mood of absolute bereavement, she comes across Harriet Vasquell, a world famous artist who has spent the last three decades living a hermit-like existence on a rustic desert estate in a national forest.

Harriet invites her to stay on to assist the old woman who will, in return, mentor our narrator as she deepens her own interest in art.

What is not at first apparent is that elements of Harriet’s past are shrouded in danger, sorrow and darkness and rather than growing as an artist, she soon finds herself enmeshed in a dangerous mystery with strands that stretch decades into the past.

```html
<!DOCTYPE html>
<html lang="en">
<head>
<meta charset="utf-8">
<title>Borrowed Lanterns — Marta K. Belloway</title>
<link rel="stylesheet" href="https://fonts.googleapis.com/css2?family=Barlow+Condensed:wght@800&family=Barlow+Semi+Condensed:wght@300&display=swap">
<style>
  :root {
    --backdrop: #282828;
    --paper: #ffffff;
    --ink: #272727;
    --ink-soft: #5f5f5f;
    --paint-red: #c4341d;
    --paint-deep: #6e120c;
  }
  html, body {
    margin: 0;
    padding: 0;
    width: 1200px;
    height: 1200px;
    overflow: hidden;
    background: var(--backdrop);
  }
  .stage {
    position: relative;
    width: 1200px;
    height: 1200px;
  }
  .book-cover {
    position: absolute;
    left: 222px;
    top: 32px;
    width: 756px;
    height: 1135px;
    background: var(--paper);
  }
  .book-cover svg {
    display: block;
    width: 756px;
    height: 1135px;
  }
  .author-name {
    font-family: "Barlow Semi Condensed", "Roboto Condensed", sans-serif;
    font-weight: 300;
    font-size: 66px;
    fill: var(--ink);
  }
  .title-line {
    font-family: "Barlow Condensed", "Oswald", sans-serif;
    font-weight: 800;
    font-size: 172px;
  }
  .title-line--primary { fill: var(--ink); }
  .title-line--secondary { fill: var(--ink-soft); }
</style>
</head>
<body>
  <main class="stage">
    <section class="book-cover" aria-label="Book cover: Borrowed Lanterns by Marta K. Belloway">
      <svg viewBox="0 0 756 1135" xmlns="http://www.w3.org/2000/svg">
        <defs>
          <radialGradient id="paint-glow" cx="0.55" cy="0.5" r="0.55">
            <stop offset="0" stop-color="var(--paint-deep)"/>
            <stop offset="0.45" stop-color="var(--paint-red)" stop-opacity="0.85"/>
            <stop offset="1" stop-color="#ffffff" stop-opacity="0"/>
          </radialGradient>
        </defs>

        <g class="cover-artwork" role="img" aria-label="Photograph of a white-painted arm reaching in from the top right, its hand dipped in glossy red paint that drips in a long thin strand toward the title">
          <rect x="200" y="0" width="556" height="800" fill="url(#paint-glow)"/>
        </g>

        <text class="author-name" x="59" y="103">Marta K. Belloway</text>

        <text class="title-line title-line--primary" x="56" y="945" textLength="644" lengthAdjust="spacingAndGlyphs">BORROWED</text>
        <text class="title-line title-line--secondary" x="700" y="1077" text-anchor="end" textLength="560" lengthAdjust="spacingAndGlyphs">LANTERNS</text>
      </svg>
    </section>
  </main>
</body>
</html>
```